"Copper Meadow" red wine label design

We are a Sydney based company. We need to design a wine label for a Australian red wine.
Front label include following info:
Our brand: "Copper Meadow";
Product name: "Shiraz 2016";
In the bottom with small font: "Wine of Australia", "750ml"
Back label:
the back label would need to be consistent with the front label, with space for one paragraph of tasting notes, and ingredient info etc.
we would like to use white, gold and blue in this label. It should make customer feel the magical and beautiful moment of starry night.

We also need a logo design for the wine brand: "Copper Meadow"

I have attached a few wine bottle that used blue to give you some inspirations.

We need the design in AI file format.

Target Market(s)

both men and women

Industry/Entity Type

It Company

Logo Text

Copper Meadow

Requirements
Nice to have
• gold borderline, words; use of blue and white

```html
<!DOCTYPE html>
<html lang="en">
<head>
<meta charset="utf-8">
<title>Copper Meadow Shiraz 2016 Label</title>
<link rel="stylesheet" href="https://fonts.googleapis.com/css2?family=Cormorant+Garamond:wght@500;600&display=swap">
<style>
  :root {
    --paper: #ffffff;
    --canvas: #ffffff;
    --ink-blue: #1c3566;
    --gold: #d9a82e;
    --gold-light: #f3d77a;
    --gold-deep: #b8861a;
    --night-top: #2b3fae;
    --night-mid: #2536a0;
    --night-bottom: #1b2a86;
    --label-edge: #3a3a3a;
  }
  * { margin: 0; padding: 0; box-sizing: border-box; }
  html, body {
    width: 1200px;
    height: 1150px;
    overflow: hidden;
    background: var(--canvas);
  }
  .canvas {
    position: relative;
    width: 1200px;
    height: 1150px;
  }
  .label {
    position: absolute;
    left: 194px;
    top: 62px;
    width: 811px;
    height: 1026px;
    background: var(--paper);
    border: 1.5px solid var(--label-edge);
    font-family: "Cormorant Garamond", Georgia, serif;
    color: var(--ink-blue);
  }
  .brand-mark {
    position: absolute;
    left: 50%;
    top: 38px;
    width: 118px;
    height: 118px;
    transform: translateX(-50%);
  }
  .brand-name {
    position: absolute;
    left: 0;
    width: 100%;
    top: 175px;
    text-align: center;
    font-size: 56px;
    font-weight: 500;
    color: var(--gold);
    letter-spacing: 1px;
    line-height: 1;
  }
  .variety {
    position: absolute;
    left: 0;
    width: 100%;
    top: 318px;
    text-align: center;
    font-size: 62px;
    font-weight: 500;
    letter-spacing: 7px;
    line-height: 1;
  }
  .vintage {
    position: absolute;
    left: 0;
    width: 100%;
    top: 376px;
    text-align: center;
    font-size: 35px;
    font-weight: 500;
    letter-spacing: 3px;
    line-height: 1;
  }
  .gold-rule {
    position: absolute;
    left: 0;
    width: 100%;
    height: 13px;
    background: linear-gradient(90deg, var(--gold-deep) 0%, var(--gold) 20%, var(--gold-light) 45%, var(--gold) 70%, var(--gold-deep) 100%);
  }
  .gold-rule--top { top: 452px; }
  .gold-rule--bottom { top: 865px; }
  .night-scene {
    position: absolute;
    left: 0;
    top: 465px;
    width: 100%;
    height: 400px;
    background:
      radial-gradient(ellipse at 70% 30%, rgba(80, 110, 210, 0.35), transparent 60%),
      linear-gradient(180deg, var(--night-top) 0%, var(--night-mid) 55%, var(--night-bottom) 100%);
  }
  .origin {
    position: absolute;
    left: 0;
    width: 100%;
    top: 912px;
    text-align: center;
    font-size: 25px;
    font-weight: 600;
    letter-spacing: 4px;
    line-height: 1;
  }
  .volume {
    position: absolute;
    left: 0;
    width: 100%;
    top: 952px;
    text-align: center;
    font-size: 23px;
    font-weight: 600;
    letter-spacing: 4px;
    line-height: 1;
  }
</style>
</head>
<body>
  <main class="canvas">
    <section class="label">
      <svg class="brand-mark" viewBox="0 0 118 118" aria-hidden="true">
        <circle cx="59" cy="59" r="55" fill="none" stroke="var(--gold)" stroke-width="5"/>
      </svg>
      <p class="brand-name">Copper Meadow</p>
      <h1 class="variety">SHIRAZ</h1>
      <p class="vintage">2016</p>
      <div class="gold-rule gold-rule--top"></div>
      <div class="night-scene" role="img" aria-label="Misty starry night sky over a farmhouse, barn and trees in deep blue tones"></div>
      <div class="gold-rule gold-rule--bottom"></div>
      <p class="origin">WINE OF AUSTRALIA</p>
      <p class="volume">750 mL</p>
    </section>
  </main>
</body>
</html>
```